Website Design for R M Builders: Showcasing Excellence in General Contracting

R M Builders, a leading general contractor based in California, is seeking a professional and engaging website design to effectively showcase our expertise, services, and commitment to excellence. The website will serve as a digital platform to represent our brand identity, highlight our portfolio, and attract potential clients in various sectors.

Key Objectives:

Reflect Company Identity: The website should accurately reflect the identity and values of R M Builders, including our dedication to quality, professionalism, and client satisfaction.
Showcase Services: Highlight our wide range of general contracting services, including but not limited to construction management, design-build, renovation, and commercial construction.
Portfolio Display: Display an extensive portfolio of past projects completed by R M Builders, showcasing our capabilities, craftsmanship, and successful outcomes.
Client Testimonials: Incorporate client testimonials and case studies to demonstrate our track record of delivering projects on time, within budget, and to the highest standards.
Contact Information: Ensure easy access to contact information, including phone number, email, and physical address, to facilitate communication with potential clients.
Responsive Design: Develop a responsive website design optimized for various devices and screen sizes, ensuring a seamless user experience across desktops, laptops, tablets, and smartphones.
Search Engine Optimization (SEO): Implement SEO best practices to enhance the visibility of the website on search engines, increasing organic traffic and generating leads.
User-Friendly Navigation: Create an intuitive and user-friendly navigation structure that enables visitors to easily find the information they need, such as services, portfolio, testimonials, and contact details.
Visual Appeal: Utilize visually appealing graphics, images, and layout designs to capture the attention of visitors and leave a lasting impression of professionalism and quality.
Compliance and Security: Ensure compliance with industry standards and regulations, as well as implementing necessary security measures to protect user data and privacy.

```html
<!DOCTYPE html>
<html lang="en">
<head>
<meta charset="utf-8">
<title>R M Builders — General Contracting</title>
<link href="https://fonts.googleapis.com/css2?family=Montserrat:wght@400;500;600;700&display=swap" rel="stylesheet">
<style>
:root{
  --orange:#f26a1b;
  --navy:#24407a;
  --ink:#2f2f2f;
  --body:#555;
  --muted:#f4f4f4;
  --line:#d9d9d9;
  --footer:#333335;
  --blue-band:#2d4c9e;
}
*{margin:0;padding:0;box-sizing:border-box}
html,body{width:1200px;height:4866px;overflow:hidden}
body{font-family:'Montserrat',sans-serif;color:var(--ink);background:#fff;position:relative}
section,header,footer{position:absolute;left:0;width:1200px}
.abs{position:absolute}
.btn{position:absolute;background:var(--orange);color:#fff;font-size:14px;font-weight:500;display:flex;align-items:center;justify-content:center;letter-spacing:.3px}
.photo{position:absolute}
.h2{position:absolute;font-size:30px;font-weight:600;color:var(--ink);letter-spacing:.3px}
.h2 b{color:var(--navy);font-weight:600}
.rule{position:absolute;height:2px;width:110px;background:#c8c8c8}

/* hero */
.hero{top:0;height:677px;background:linear-gradient(180deg,#6e5a44 0%,#8a6a48 45%,#5d4632 100%)}
.hero .shade{position:absolute;inset:0;background:rgba(0,0,0,.25)}
.logo-tab{position:absolute;left:75px;top:0;width:205px;height:189px;background:#eee;border-radius:0 0 100px 100px;display:flex;flex-direction:column;align-items:center;justify-content:center}
.logo-tab .name{font-size:22px;font-weight:700;color:#111}
.logo-tab .place{font-size:13px;font-weight:700;color:#111;margin-top:6px}
.nav{position:absolute;top:98px;left:445px;display:flex;gap:33px;font-size:14px;font-weight:500;color:#fff}
.nav .active{border-bottom:2px solid var(--orange);padding-bottom:2px}
.phone-ico{position:absolute;left:907px;top:26px;width:38px;height:36px;background:#7a7a7a;display:flex;align-items:center;justify-content:center}
.phone-num{position:absolute;left:955px;top:26px;width:173px;height:36px;background:var(--orange);color:#fff;font-size:19px;font-weight:500;display:flex;align-items:center;justify-content:center}
.hero-title{position:absolute;top:295px;width:1200px;text-align:center;color:#fff;font-size:60px;font-weight:500;letter-spacing:1px}
.hero-sub{position:absolute;top:365px;width:1200px;text-align:center;color:#fff;font-size:30px;font-weight:500;line-height:35px}

/* about */
.about{top:677px;height:514px}
.about p{position:absolute;left:616px;top:186px;width:515px;font-size:13px;line-height:25.5px;color:var(--body)}

/* services */
.services{top:1191px;height:625px;background:var(--muted)}
.arrow{position:absolute;width:24px;height:24px}
.svc{position:absolute;top:143px;width:330px}
.svc .photo{position:relative;height:237px}
.svc h3{font-size:19px;font-weight:600;color:var(--navy);margin-top:22px}
.svc p{font-size:13px;line-height:25.5px;color:var(--body);margin-top:6px}
.svc .btn{position:relative;width:136px;height:40px;margin-top:24px}

/* projects */
.projects{top:1816px;height:892px}

/* experience */
.experience{top:2708px;height:511px;background:var(--muted)}
.experience .lead{position:absolute;top:160px;left:80px;width:1040px;text-align:center;font-size:13px;line-height:25.5px;color:var(--body)}
.exp-card{position:absolute;top:237px;width:181px;height:198px;background:#fff;box-shadow:0 0 8px rgba(0,0,0,.1);text-align:center}
.exp-card svg{margin-top:34px}
.exp-card span{display:block;margin-top:12px;font-size:14.5px;line-height:20px;color:var(--navy)}

/* testimonials */
.testimonials{top:3219px;height:414px}
.quote{position:absolute;top:136px;width:330px;height:208px;border:1px solid var(--line);padding:24px 16px}
.quote p{font-size:13px;line-height:24px;font-style:italic;color:var(--ink);margin-top:10px}
.who{display:flex;align-items:center;gap:14px;margin-top:18px}
.avatar{width:44px;height:44px;border-radius:50%;background:#333}
.who b{display:block;font-size:14px;font-weight:600;color:var(--navy)}
.who small{font-size:12px;color:var(--body)}

/* general contracting */
.general{top:3633px;height:434px;background:linear-gradient(180deg,#2f4f9f 0%,#28458f 100%)}
.general .h2{color:#fff;width:1200px;text-align:center;top:52px}
.checks{position:absolute;top:155px;font-size:14px;color:#fff;line-height:34.5px}
.checks li{list-style:none;display:flex;align-items:center;gap:14px}

/* contact */
.contact{top:4067px;height:513px}
.field{position:absolute;border:1px solid var(--line);font-size:11px;color:#666;padding:14px 12px}

/* footer */
.footer{top:4580px;height:286px;background:var(--footer);color:#fff}
.footer h4{font-size:14px;font-weight:600;letter-spacing:.3px}
.col{position:absolute;top:52px;font-size:12px;line-height:25px;color:#eee}
.footer .brand{position:absolute;left:75px;top:62px;width:150px;text-align:center}
.social{display:flex;gap:12px;margin-top:12px}
.social i{width:20px;height:20px;border-radius:50%;background:#fff;display:block}
</style>
</head>
<body>

<header class="hero">
  <div class="shade" role="img" aria-label="Excavator moving earth on a construction site at dusk"></div>
  <div class="logo-tab"><span class="name">R M BUILDERS</span><span class="place">SANTA MARIA, CA</span></div>
  <nav class="nav"><span class="active">Home</span><span>About Us</span><span>Services</span><span>Project Gallery</span><span>Testimonials</span><span>Blog</span><span>Contact Us</span></nav>
  <div class="phone-ico"><svg width="18" height="18" viewBox="0 0 24 24" fill="#fff"><path d="M6.6 10.8a15 15 0 0 0 6.6 6.6l2.2-2.2c.3-.3.7-.4 1-.2 1.1.4 2.3.6 3.6.6.6 0 1 .4 1 1V20c0 .6-.4 1-1 1A17 17 0 0 1 3 4c0-.6.4-1 1-1h3.5c.6 0 1 .4 1 1 0 1.3.2 2.5.6 3.6.1.3 0 .7-.2 1z"/></svg></div>
  <div class="phone-num">(805) 555-0142</div>
  <h1 class="hero-title">RM BUILDERS</h1>
  <div class="hero-sub">An 8(a) Small Business<br>Prime Contractor</div>
  <div class="btn" style="left:524px;top:459px;width:151px;height:42px">CONTACT US</div>
</header>

<section class="about">
  <div class="photo" style="left:74px;top:60px;width:514px;height:378px;background:linear-gradient(180deg,#9fb7c9 0%,#c9b48a 55%,#a26a3b 100%)" role="img" aria-label="Yellow excavator digging sandy soil"></div>
  <h2 class="h2" style="left:616px;top:112px">ABOUT <b>R M BUILDERS</b></h2>
  <p>Dan Hollis, the sole owner and CEO/President of R M Builders (RMB) originally started the company in 2013. Since, RMB has been a thriving 8(a) certified General Contractor, consistently deliv The company has developed experience with civil, concrete, paving, grading and other small purchase order type projects.</p>
  <div class="btn" style="left:616px;top:334px;width:151px;height:44px">READ MORE</div>
</section>

<section class="services">
  <h2 class="h2" style="left:74px;top:60px">SERVICES OFFERED</h2>
  <div class="rule" style="left:74px;top:105px"></div>
  <svg class="arrow" style="left:1061px;top:65px" viewBox="0 0 24 24"><circle cx="12" cy="12" r="12" fill="#bdbdbd"/><path d="M14 7l-5 5 5 5" stroke="#fff" stroke-width="2.2" fill="none"/></svg>
  <svg class="arrow" style="left:1103px;top:65px" viewBox="0 0 24 24"><circle cx="12" cy="12" r="12" fill="var(--navy)"/><path d="M10 7l5 5-5 5" stroke="#fff" stroke-width="2.2" fill="none"/></svg>
  <div class="svc" style="left:74px"><div class="photo" style="background:linear-gradient(180deg,#c8cdd2,#9c8a72)" role="img" aria-label="Excavator demolishing an old building"></div><h3>DEMOLITION</h3><p>Nemo enim ipsam voluptatem quia voluptas sit aspernatur aut odit aut fugit, sed quia cons equuntur magni dolores.</p><div class="btn">MORE INFO</div></div>
  <div class="svc" style="left:435px"><div class="photo" style="background:linear-gradient(180deg,#3f7f96,#e58a3a 60%,#4a3324)" role="img" aria-label="Excavator at sunset in front of high-rise construction"></div><h3>EXCAVATION</h3><p>Nemo enim ipsam voluptatem quia voluptas sit aspernatur aut odit aut fugit, sed quia cons equuntur magni dolores.</p><div class="btn">MORE INFO</div></div>
  <div class="svc" style="left:797px"><div class="photo" style="background:linear-gradient(135deg,#2e4a8c,#c45a3a 60%,#d0a050)" role="img" aria-label="Electrician working on an industrial control panel"></div><h3>ELECTRIC MAINTENANCE</h3><p>Nemo enim ipsam voluptatem quia voluptas sit aspernatur aut odit aut fugit, sed quia cons equuntur magni dolores.</p><div class="btn">MORE INFO</div></div>
</section>

<section class="projects">
  <h2 class="h2" style="width:1200px;text-align:center;top:52px">PAST <b>PROJECTS</b></h2>
  <div class="rule" style="left:545px;top:100px"></div>
  <div class="photo" style="left:74px;top:150px;width:514px;height:277px;background:linear-gradient(180deg,#8fb0cc,#7d8a6a 45%,#8a7a5e)" role="img" aria-label="Utility trucks on a hillside road"></div>
  <div class="photo" style="left:616px;top:150px;width:242px;height:277px;background:linear-gradient(180deg,#6fa3d8,#8a8f94)" role="img" aria-label="Electrical substation transformer"></div>
  <div class="photo" style="left:886px;top:150px;width:242px;height:277px;background:linear-gradient(180deg,#d99a5a,#8a6a52 60%,#4c4a4a)" role="img" aria-label="Freight truck on a highway at sunset"></div>
  <div class="photo" style="left:74px;top:458px;width:242px;height:277px;background:linear-gradient(90deg,#3a3e44,#9aa0a6,#3a3e44)" role="img" aria-label="Glass elevator shafts"></div>
  <div class="photo" style="left:346px;top:458px;width:242px;height:277px;background:linear-gradient(180deg,#a7a39c,#6e6a64)" role="img" aria-label="Concrete being poured from a shovel"></div>
  <div class="photo" style="left:616px;top:458px;width:512px;height:277px;background:linear-gradient(180deg,#6d7275,#a4a9a8)" role="img" aria-label="Engineers walking through a concrete structure site"></div>
  <div class="btn" style="left:499px;top:783px;width:202px;height:45px">VIEW ALL PROJECTS</div>
</section>

<section class="experience">
  <h2 class="h2" style="width:1200px;text-align:center;top:72px">EXPERIENCE</h2>
  <div class="rule" style="left:545px;top:124px"></div>
  <p class="lead">With vast experience in the trades, site superintendence, safety, quality control, and all aspects of general contracting, R M Builders can plan, manage and execute building construction projects in all sizes under any delivery method: design-build, CM at Risk, or design-bid-build.</p>
  <div class="exp-card" style="left:74px"><svg width="76" height="76" viewBox="0 0 76 76" fill="none" stroke="var(--orange)" stroke-width="2"><circle cx="38" cy="38" r="10"/><circle cx="14" cy="14" r="8"/><circle cx="62" cy="14" r="8"/><circle cx="14" cy="62" r="8"/><circle cx="62" cy="62" r="8"/><circle cx="38" cy="8" r="5"/><circle cx="38" cy="68" r="5"/><path d="M20 20l10 10M56 20L46 30M20 56l10-10M56 56L46 46"/></svg><span>Quickly mobilize<br>assets + personnel</span></div>
  <div class="exp-card" style="left:293px"><svg width="76" height="76" viewBox="0 0 76 76" fill="none" stroke="var(--orange)" stroke-width="2"><path d="M26 6h24l6 10 12 4v50H8V20l12-4z"/><path d="M30 6v64M46 6v64M8 40h60M8 50h60"/></svg><span>Commitment to<br>quality + safety</span></div>
  <div class="exp-card" style="left:510px"><svg width="76" height="76" viewBox="0 0 76 76" fill="none" stroke="var(--orange)" stroke-width="2"><path d="M20 16c0-8 20-8 20 0M14 28c-6 10-6 34 16 38 16 0 20-18 16-30-2-6-6-8-8-8H22z"/><text x="24" y="56" font-size="22" fill="var(--orange)" stroke="none" font-family="Montserrat,sans-serif">$</text><rect x="46" y="34" width="24" height="34"/><path d="M50 40h16M50 48h4M58 48h4M50 56h4M58 56h4M50 62h4M58 62h4"/></svg><span>Complete projects<br>on time + on budget</span></div>
  <div class="exp-card" style="left:728px"><svg width="76" height="76" viewBox="0 0 76 76" fill="none" stroke="var(--orange)" stroke-width="2"><circle cx="38" cy="14" r="9"/><path d="M24 30h28M28 30a10 10 0 0 0 20 0M16 70V56c0-8 10-14 22-14s22 6 22 14v14M30 44l8 14 8-14"/><circle cx="16" cy="38" r="6"/><circle cx="60" cy="38" r="6"/></svg><span>Qualified field +<br>office staff</span></div>
  <div class="exp-card" style="left:947px"><svg width="76" height="76" viewBox="0 0 76 76" fill="none" stroke="var(--orange)" stroke-width="2"><path d="M8 24h20l6 6h30v40H8z"/><circle cx="34" cy="16" r="9"/><path d="M30 28h8M68 8L56 52M58 8h12v10"/><circle cx="30" cy="52" r="8"/><path d="M30 40v4M30 60v4M18 52h4M38 52h4"/></svg><span>Value<br>engineering</span></div>
</section>

<section class="testimonials">
  <h2 class="h2" style="left:74px;top:52px">CLIENT <b>TESTIMONIALS</b></h2>
  <div class="rule" style="left:74px;top:97px"></div>
  <svg class="arrow" style="left:1061px;top:55px" viewBox="0 0 24 24"><circle cx="12" cy="12" r="12" fill="#bdbdbd"/><path d="M14 7l-5 5 5 5" stroke="#fff" stroke-width="2.2" fill="none"/></svg>
  <svg class="arrow" style="left:1103px;top:55px" viewBox="0 0 24 24"><circle cx="12" cy="12" r="12" fill="var(--navy)"/><path d="M10 7l5 5-5 5" stroke="#fff" stroke-width="2.2" fill="none"/></svg>
  <div class="quote" style="left:74px"><svg width="78" height="13" viewBox="0 0 78 13" fill="var(--orange)"><g id="st"><polygon points="6.5,0 8.2,4.5 13,4.7 9.2,7.6 10.5,12.3 6.5,9.6 2.5,12.3 3.8,7.6 0,4.7 4.8,4.5"/></g><use href="#st" x="16"/><use href="#st" x="32"/><use href="#st" x="48"/><use href="#st" x="64"/></svg><p>“ Natus error sit voluptatem accusantium doloremque laudantium, totam rem aperiam, eaque ipsa quae ab illo inventore..”</p><div class="who"><div class="avatar"></div><div><b>NAME HEADING</b><small>Location</small></div></div></div>
  <div class="quote" style="left:435px"><svg width="78" height="13" viewBox="0 0 78 13" fill="var(--orange)"><use href="#st"/><use href="#st" x="16"/><use href="#st" x="32"/><use href="#st" x="48"/><use href="#st" x="64"/></svg><p>“ Natus error sit voluptatem accusantium doloremque laudantium, totam rem aperiam, eaque ipsa quae ab illo inventore..”</p><div class="who"><div class="avatar"></div><div><b>NAME HEADING</b><small>Location</small></div></div></div>
  <div class="quote" style="left:797px"><svg width="78" height="13" viewBox="0 0 78 13" fill="var(--orange)"><use href="#st"/><use href="#st" x="16"/><use href="#st" x="32"/><use href="#st" x="48"/><use href="#st" x="64"/></svg><p>“ Natus error sit voluptatem accusantium doloremque laudantium, totam rem aperiam, eaque ipsa quae ab illo inventore..”</p><div class="who"><div class="avatar"></div><div><b>NAME HEADING</b><small>Location</small></div></div></div>
</section>

<section class="general" role="img" aria-label="Construction workers and excavator under a blue overlay">
  <h2 class="h2">GENERAL CONTRACTING</h2>
  <div class="rule" style="left:545px;top:100px;background:#fff"></div>
  <ul class="checks" style="left:234px"><li><svg width="16" height="16" viewBox="0 0 16 16" fill="none" stroke="#fff" stroke-width="1.5"><circle cx="8" cy="8" r="7"/><path d="M4.5 8l2.5 2.5 4.5-5"/></svg>Preconstruction</li><li><svg width="16" height="16" viewBox="0 0 16 16" fill="none" stroke="#fff" stroke-width="1.5"><circle cx="8" cy="8" r="7"/><path d="M4.5 8l2.5 2.5 4.5-5"/></svg>Constructability Review</li><li><svg width="16" height="16" viewBox="0 0 16 16" fill="none" stroke="#fff" stroke-width="1.5"><circle cx="8" cy="8" r="7"/><path d="M4.5 8l2.5 2.5 4.5-5"/></svg>Value Engineering</li><li><svg width="16" height="16" viewBox="0 0 16 16" fill="none" stroke="#fff" stroke-width="1.5"><circle cx="8" cy="8" r="7"/><path d="M4.5 8l2.5 2.5 4.5-5"/></svg>Program Management</li></ul>
  <ul class="checks" style="left:507px"><li><svg width="16" height="16" viewBox="0 0 16 16" fill="none" stroke="#fff" stroke-width="1.5"><circle cx="8" cy="8" r="7"/><path d="M4.5 8l2.5 2.5 4.5-5"/></svg>Design-Build</li><li><svg width="16" height="16" viewBox="0 0 16 16" fill="none" stroke="#fff" stroke-width="1.5"><circle cx="8" cy="8" r="7"/><path d="M4.5 8l2.5 2.5 4.5-5"/></svg>Project Management</li><li><svg width="16" height="16" viewBox="0 0 16 16" fill="none" stroke="#fff" stroke-width="1.5"><circle cx="8" cy="8" r="7"/><path d="M4.5 8l2.5 2.5 4.5-5"/></svg>Safety Management</li><li><svg width="16" height="16" viewBox="0 0 16 16" fill="none" stroke="#fff" stroke-width="1.5"><circle cx="8" cy="8" r="7"/><path d="M4.5 8l2.5 2.5 4.5-5"/></svg>Jobsite Supervision</li></ul>
  <ul class="checks" style="left:773px"><li><svg width="16" height="16" viewBox="0 0 16 16" fill="none" stroke="#fff" stroke-width="1.5"><circle cx="8" cy="8" r="7"/><path d="M4.5 8l2.5 2.5 4.5-5"/></svg>Quality Control</li><li><svg width="16" height="16" viewBox="0 0 16 16" fill="none" stroke="#fff" stroke-width="1.5"><circle cx="8" cy="8" r="7"/><path d="M4.5 8l2.5 2.5 4.5-5"/></svg>Service &amp; Maintenance</li><li><svg width="16" height="16" viewBox="0 0 16 16" fill="none" stroke="#fff" stroke-width="1.5"><circle cx="8" cy="8" r="7"/><path d="M4.5 8l2.5 2.5 4.5-5"/></svg>Risk Analysis</li><li><svg width="16" height="16" viewBox="0 0 16 16" fill="none" stroke="#fff" stroke-width="1.5"><circle cx="8" cy="8" r="7"/><path d="M4.5 8l2.5 2.5 4.5-5"/></svg>Estimating</li></ul>
  <div class="btn" style="left:524px;top:328px;width:151px;height:46px">CONTACT US</div>
</section>

<section class="contact">
  <div class="photo" style="left:74px;top:68px;width:514px;height:376px;background:linear-gradient(180deg,#c8ad84,#b4965e 50%,#6f5a3a)" role="img" aria-label="Site engineer in hard hat and safety vest holding a tablet"></div>
  <h2 class="h2" style="left:616px;top:76px"><b>CONTACT US</b></h2>
  <div class="abs" style="left:616px;top:138px;font-size:12px;color:var(--body)">Interested in working with us?</div>
  <div class="field" style="left:616px;top:172px;width:248px;height:44px">Name</div>
  <div class="field" style="left:877px;top:172px;width:249px;height:44px">Email Address</div>
  <div class="field" style="left:616px;top:231px;width:248px;height:43px">Phone No</div>
  <div class="field" style="left:877px;top:231px;width:249px;height:43px">Subject</div>
  <div class="field" style="left:616px;top:289px;width:510px;height:93px">Message</div>
  <div class="btn" style="left:616px;top:403px;width:151px;height:41px">SUBMIT</div>
</section>

<footer class="footer">
  <div class="brand"><div style="font-size:18px;font-weight:700">R M BUILDERS</div><div style="font-size:11px;font-weight:700;margin-top:4px">SANTA MARIA, CA</div></div>
  <div class="abs" style="left:75px;top:182px;font-size:12px;line-height:20px;color:#eee">Copyright © 2024 Company Name.<br>All Rights Reserved</div>
  <div class="col" style="left:368px"><h4>SITE MAP</h4><div style="margin-top:6px">Home<br>About Us<br>Services<br>Project Gallery<br>Testimonials<br>Blog<br>Contact Us</div></div>
  <div class="col" style="left:567px;width:300px"><h4>CONTACT INFO</h4>
    <div style="display:flex;gap:12px;margin-top:6px;line-height:22px"><svg width="16" height="14" viewBox="0 0 16 14" style="margin-top:4px;flex:none"><path d="M2 1v12" stroke="var(--orange)" stroke-width="2"/><path d="M3 1h11l-3 4 3 4H3z" fill="var(--orange)"/></svg><span>412 Mesa Ridge Road, Santa Maria,<br>California 93454, United States</span></div>
    <div style="display:flex;gap:12px;margin-top:6px"><svg width="16" height="16" viewBox="0 0 24 24" fill="var(--orange)" style="margin-top:4px"><path d="M6.6 10.8a15 15 0 0 0 6.6 6.6l2.2-2.2c.3-.3.7-.4 1-.2 1.1.4 2.3.6 3.6.6.6 0 1 .4 1 1V20c0 .6-.4 1-1 1A17 17 0 0 1 3 4c0-.6.4-1 1-1h3.5c.6 0 1 .4 1 1 0 1.3.2 2.5.6 3.6.1.3 0 .7-.2 1z"/></svg>(805) 555-0142</div>
    <div style="display:flex;gap:12px;margin-top:4px"><svg width="16" height="12" viewBox="0 0 16 12" style="margin-top:7px"><rect width="16" height="12" fill="var(--orange)"/><path d="M0 0l8 6 8-6" stroke="#fff" fill="none"/></svg>hello@rmbuilders.biz</div>
  </div>
  <div class="col" style="left:884px;width:240px"><h4>HOURS</h4><div style="margin-top:6px;line-height:29px">Monday - Friday: 730am - 430pm<br>Saturday - Sunday: Closed</div><h4 style="margin-top:20px">FOLLOW US</h4><div class="social"><i></i><i></i><i></i><i></i><i></i></div></div>
</footer>

</body>
</html>
```